Counseling Practice Business Card

I need a professional looking business card incorporating my new logo that was just completed. Card needs to incorporate my name and title, description of my specialty, my address, my phone number, my fax number, my email and my website URL. I need to be able to choose design on/with different paper colors and textures.
I do not have a lot of business card ideas so I am open to anything but I want bold,sharp, clear card without additional designs other than my logo (see attached file info). I am open to different color backgrounds or paper colors including black. I do not like traditional brackets around area codes in phone number or dashes between numbers in phone number. Am open to other ways of presenting including periods between numbers as appropriate. I do not know enough to know what I like yet but I want card to coordinate and work together with my logo. My practice emphasizes natural mental health interventions so any use of color (with background paper color or the blue and green in my logo) that elicits nature is nice. In addition to black, any natural brown or wood looking background might be desirable also. Most of the offerings so far look very similar and boring.

Target Market(s)

Potential therapy clients and other professionals

Contact Information for Business Card

Card information:
Marcus T. Whitfield, Ph.D.
Licensed Clinical Psychologist
Integrative Health Coach
4812 Ferndale Pkwy NW
Suite 730
Harlow Springs, GA 30187
(770) 555-0142 phone
(770) 555-0186 fax
drmarcuswhitfield@kelvora.com
pathbloomcounseling.com

Font styles to use
Serif
Sans Serif
Other font styles liked:
• anything that you think looks crisp, clear and easily readable

Requirements
Must have
• Any color used should coordinate with my logo design (see attached files).
• Card should be printed horizontally so top and bottom are longest sides of rectangle.
• Background color or paper color should complement and highlight logo. Do not like a white background. black, grey, brown or any color my logo would blend well with.
Nice to have
• I would like designer to utilize color to highlight letters/name or phone-fax-web symbols.
• Bottom edge of card could be highlighted if appropriate to an idea.
Should not have
• I would NOT want the card to have a pure white background at all.
• No clear cards.
• Cards should be oriented with long sides on bottom and top, NOT sides. DO NOT LIKE THIS THIN TALL ORIENTATION.

```html
<!DOCTYPE html>
<html lang="en">
<head>
<meta charset="utf-8">
<title>Pathbloom Counseling – Business Card</title>
<link href="https://fonts.googleapis.com/css2?family=Montserrat:wght@600;700&family=Questrial&display=swap" rel="stylesheet">
<style>
  :root {
    --backdrop: #e4e5e7;
    --paper: #f6f6f4;
    --brand-blue: #2a72b8;
    --brand-green: #137035;
    --ink-white: #ffffff;
    --rule: rgba(255,255,255,0.55);
  }
  * { margin: 0; padding: 0; box-sizing: border-box; }
  html, body {
    width: 1200px; height: 900px; overflow: hidden;
    background: var(--backdrop);
    font-family: "Questrial", "Helvetica Neue", Arial, sans-serif;
  }
  .canvas {
    width: 1200px; height: 900px;
    display: flex; flex-direction: column; align-items: center; justify-content: center;
    gap: 60px;
  }
  .card {
    position: relative;
    width: 630px; height: 360px;
    background: var(--paper);
    overflow: hidden;
    box-shadow: 0 6px 18px rgba(0,0,0,0.15);
  }
  .brand-name {
    font-family: "Montserrat", Arial, sans-serif;
    font-weight: 600;
    color: var(--brand-blue);
    letter-spacing: 0.5px;
  }

  /* Front */
  .front .brand-name { position: absolute; left: 38px; top: 48px; font-size: 30px; }
  .front .band-blue {
    position: absolute; left: 0; top: 130px; width: 100%; height: 172px;
    background: var(--brand-blue); color: var(--ink-white);
  }
  .front .band-green {
    position: absolute; left: 0; bottom: 0; width: 100%; height: 58px;
    background: var(--brand-green);
  }
  .holder-name {
    position: absolute; left: 38px; top: 20px;
    font-family: "Montserrat", Arial, sans-serif; font-weight: 700; font-size: 20px;
  }
  .holder-title { position: absolute; left: 38px; top: 50px; font-size: 13px; }
  .title-rule {
    position: absolute; left: 340px; right: 0; top: 34px;
    border-top: 1px solid var(--rule);
  }
  .address-rule {
    position: absolute; left: 38px; width: 220px; top: 82px;
    border-top: 1px solid var(--rule);
  }
  .address {
    position: absolute; left: 38px; top: 96px;
    font-size: 14px; line-height: 20px; font-style: normal;
  }
  .contact-list {
    position: absolute; left: 300px; top: 96px; list-style: none;
    font-size: 14px; line-height: 20px;
  }
  .contact-list li { display: flex; align-items: center; gap: 8px; }
  .contact-list svg { width: 12px; height: 12px; fill: var(--ink-white); flex: none; }
  .front .website {
    position: absolute; left: 300px; top: 20px;
    color: var(--ink-white); font-size: 14px;
  }

  /* Back */
  .back { display: flex; flex-direction: column; align-items: center; justify-content: center; gap: 14px; }
  .back .brand-name { font-size: 40px; }
  .back .website { color: var(--brand-green); font-size: 15px; letter-spacing: 1px; }
</style>
</head>
<body>
<main class="canvas">
  <section class="card front" aria-label="Business card front">
    <div class="brand-name">Pathbloom Counseling</div>
    <div class="band-blue">
      <h1 class="holder-name">Marcus T. Whitfield, Ph.D.</h1>
      <p class="holder-title">Licensed Clinical Psychologist | Integrative Health Coach</p>
      <div class="title-rule"></div>
      <div class="address-rule"></div>
      <address class="address">4812 Ferndale Pkwy NW<br>Suite 730<br>Harlow Springs, GA 30187</address>
      <ul class="contact-list">
        <li><svg viewBox="0 0 24 24" aria-hidden="true"><path d="M6.6 10.8a15 15 0 0 0 6.6 6.6l2.2-2.2c.3-.3.7-.4 1-.2 1.1.4 2.3.6 3.6.6.6 0 1 .4 1 1V20c0 .6-.4 1-1 1A17 17 0 0 1 3 4c0-.6.4-1 1-1h3.5c.6 0 1 .4 1 1 0 1.3.2 2.5.6 3.6.1.3 0 .7-.2 1z"/></svg>770.555.0142</li>
        <li><svg viewBox="0 0 24 24" aria-hidden="true"><path d="M6 2h12v6H6zM3 9h18a1 1 0 0 1 1 1v7h-4v5H6v-5H2v-7a1 1 0 0 1 1-1zm5 7v4h8v-4z"/></svg>770.555.0186</li>
        <li><svg viewBox="0 0 24 24" aria-hidden="true"><path d="M2 5h20v14H2zm2 2v.5l8 5 8-5V7zm0 2.8V17h16V9.8l-8 5z"/></svg>drmarcuswhitfield@kelvora.com</li>
      </ul>
    </div>
    <div class="band-green">
      <p class="website">www.pathbloomcounseling.com</p>
    </div>
  </section>

  <section class="card back" aria-label="Business card back">
    <div class="brand-name">Pathbloom Counseling</div>
    <p class="website">www.pathbloomcounseling.com</p>
  </section>
</main>
</body>
</html>
```